Counselling business requires poster

I require a poster to promote my counselling and coaching business I will be placing these in doctors surgery's and clinics etc.
This business is centred around helping people work through emotional issues. We provided one on one sessions which help enhance peoples lives by assisting them in overcoming their fears, obsessions, insecurities etc.

We offer support in a broad range of areas:

- Eating disorders & weight managment
- Depression
- Marriage and relationship issues
- Anxiety
- Victims of physical, verbal and/or social abuse

We want our poster to be representative of the positive, warm and welcoming atmosphere we provide.

Our motto, 'One step at a time', is symbolic of our approach and how we help our clients to tackle their problems bit by bit.

The flyer I have uploaded is just some information on what we offer

Thankyou for your designs I am taking them into consideration and will inform you of any decision.

```html
<!DOCTYPE html>
<html lang="en">
<head>
<meta charset="utf-8">
<title>One Step at a Time – Counselling Poster</title>
<link href="https://fonts.googleapis.com/css2?family=Crimson+Text&family=Reenie+Beanie&display=swap" rel="stylesheet">
<style>
  :root {
    --backdrop: #1f6e96;
    --sky-top: #8fb3d6;
    --sky-mid: #bcd8e2;
    --sky-low: #dfe9e4;
    --trouser-red: #d9485a;
    --grass-green: #8a9c4e;
    --grass-dark: #5c6a3a;
    --paper: #ffffff;
    --service-pink: #e0667a;
    --brand-navy: #2b2754;
    --brand-gold: #e3a72f;
  }
  * { margin: 0; padding: 0; box-sizing: border-box; }
  html, body {
    width: 1009px;
    height: 1200px;
    overflow: hidden;
    background: var(--backdrop);
  }
  .poster {
    position: absolute;
    left: 0;
    top: 77px;
    width: 1009px;
    height: 1045px;
    overflow: hidden;
    background: var(--paper);
  }
  .hero-photo {
    position: absolute;
    left: 0; top: 0;
    width: 1009px; height: 878px;
    background:
      radial-gradient(ellipse 55% 40% at 70% 60%, rgba(217,72,90,0.85), rgba(217,72,90,0) 70%),
      radial-gradient(ellipse 30% 30% at 68% 20%, rgba(250,245,235,0.9), rgba(250,245,235,0) 70%),
      linear-gradient(180deg, rgba(0,0,0,0) 80%, rgba(110,90,80,0.55) 100%),
      linear-gradient(160deg, var(--sky-top) 0%, var(--sky-mid) 55%, var(--sky-low) 100%);
  }
  .headline-group {
    position: absolute;
    left: 0; top: 0;
    width: 1009px; height: 878px;
    margin: 0;
    font-size: 16px;
    font-weight: 400;
  }
  .headline {
    position: absolute;
    font-family: "Reenie Beanie", cursive;
    font-weight: 400;
    color: var(--paper);
    line-height: 1;
    white-space: nowrap;
  }
  .headline-one  { left: 112px; top: 350px; font-size: 170px; letter-spacing: 8px; }
  .headline-step { left: 474px; top: 300px; font-size: 230px; letter-spacing: 4px; }
  .headline-time { left: 230px; top: 478px; font-size: 150px; letter-spacing: 6px; word-spacing: 36px; }
  .service-band {
    position: absolute;
    left: 0; top: 878px;
    width: 1009px; height: 82px;
    background: var(--paper);
  }
  .service-list {
    position: absolute;
    left: 194px; top: 18px;
    font-family: "Crimson Text", serif;
    font-size: 20px;
    line-height: 23px;
    color: var(--service-pink);
    white-space: nowrap;
  }
  .service-list .divider { margin: 0 11px; }
  .brand {
    position: absolute;
    left: 872px; top: 29px;
    display: flex;
    align-items: center;
    gap: 5px;
    font-family: "Crimson Text", serif;
    font-size: 16px;
    line-height: 1;
    color: var(--brand-navy);
  }
  .brand-dot {
    width: 12px; height: 12px;
    border-radius: 50%;
    background: var(--brand-gold);
  }
  .contact-strip {
    position: absolute;
    left: 0; top: 960px;
    width: 1009px; height: 85px;
    background: linear-gradient(180deg, #9aa07a 0%, var(--grass-green) 45%, var(--grass-dark) 100%);
  }
  .contact-text {
    position: absolute;
    top: 18px;
    font-family: "Reenie Beanie", cursive;
    font-size: 52px;
    line-height: 1;
    color: rgba(255,255,255,0.8);
    letter-spacing: 4px;
    white-space: nowrap;
  }
  .contact-phone { left: 124px; }
  .contact-web { left: 600px; }
</style>
</head>
<body>
  <main class="poster">
    <div class="hero-photo" role="img" aria-label="Photograph of a woman in a white top and red trousers leaping joyfully against a blue sky, holding a red heart balloon, with bare trees and grass below"></div>

    <h1 class="headline-group">
      <span class="headline headline-one">One</span>
      <span class="headline headline-step">Step</span>
      <span class="headline headline-time">at a Time</span>
    </h1>

    <section class="service-band">
      <p class="service-list">
        Eating disorders &amp; weight managment<span class="divider">|</span>Marriage and relationship issues<br>
        Depression<span class="divider">|</span>Anxiety<span class="divider">|</span>Victims of physical, verbal and/or social abuse
      </p>
      <div class="brand"><span class="brand-dot"></span>WAYPOINTS</div>
    </section>

    <footer class="contact-strip" role="img" aria-label="Photograph of a sunlit grassy meadow">
      <span class="contact-text contact-phone">call 08 555 0142</span>
      <span class="contact-text contact-web">www.waypoints.com</span>
    </footer>
  </main>
</body>
</html>
```